Food packaging label design

The product name Crisplets, a thin, crispy, and delicious biscuit/cookie made from simple, all natural ingredients. Its name comes from the fact that it looks and tastes a lot like a biscotti cookie, but thinly sliced and much crispier and more delicious than a biscotti. There are currently two flavors: Pure Harvest, and Maple Orchard.

I am looking for a fresh, eye catchy design to go on the label for a rice paper stand up pouch (pouch sample attached). Label size are as follows:

4 oz bag - Width X Height
top: 4.5" x 3.5" bottom: 4.5" x 1.5"

12 oz bag
top: 6.5" x 5.5" bottom: 6.5" x 1.5"

I would like for the top portion of the packaging to include:

Crisplets name
Tag line " a thinner, crispier, and more delicious cousin to the biscotti"
simple and natural ingredients

bottom to include:
net weight
ingredients: wheat flour, eggs, sugar, almonds

Attached is a copy of something I created in powerpoint. you can recreate this using graphic designer software per label specs and improve on it or supprise me with something totally awesome. The key is that it that the colors and design needs to pop or contrast against the white rice paper bag and design needs to be eye catchy, fun and whimsical.

Please refer to link below for best practices for creating artwork for labels to ensure correct format for printing.
http://www.printwellmark.example/label-articles/best-practices-designing-custom-labels/

Good luck!
Updates

Target Market(s)

educated, health conscious consumers such as customers who shops at green basket, brewhollow, market pennys

Industry/Entity Type

Graphic Designer

Requirements
Should not have
• busy or clutter design

```html
<!DOCTYPE html>
<html lang="en">
<head>
<meta charset="utf-8">
<title>Crisplets – Maple Orchard label</title>
<link rel="stylesheet" href="https://fonts.googleapis.com/css2?family=Gochi+Hand&family=Kalam:wght@400&family=Delius&display=swap">
<style>
  :root {
    --title-white: #ffffff;
    --title-outline: #8a5a14;
    --tagline-red: #b5122e;
    --band-green: #3cbd16;
    --band-white: #fbfbf9;
    --flavor-bg: #a9601f;
    --ink: #111111;
    --warm-brown: #9a5a1c;
    --warm-orange: #d9922c;
    --warm-gold: #e8c45a;
  }
  * { margin: 0; padding: 0; box-sizing: border-box; }
  html, body { width: 1200px; height: 1015px; overflow: hidden; background: var(--band-white); }
  .label {
    position: relative;
    width: 1200px;
    height: 1015px;
    overflow: hidden;
    background: var(--band-white);
  }
  .food-photo {
    position: absolute;
    left: 0;
    width: 1200px;
  }
  .food-photo--top {
    top: 0;
    height: 540px;
    background: linear-gradient(180deg,
      var(--warm-brown) 0%,
      var(--warm-orange) 30%,
      var(--warm-gold) 62%,
      rgba(251,251,249,0) 100%);
  }
  .food-photo--bottom {
    top: 820px;
    height: 195px;
    background: linear-gradient(180deg,
      rgba(251,251,249,0) 0%,
      var(--warm-gold) 55%,
      var(--warm-orange) 100%);
  }
  .band-green {
    position: absolute;
    left: 0;
    top: 580px;
    width: 1200px;
    height: 200px;
    background: linear-gradient(180deg,
      rgba(60,189,22,0) 0%,
      var(--band-green) 20%,
      var(--band-green) 80%,
      rgba(60,189,22,0) 100%);
  }
  .product-name {
    position: absolute;
    left: 0;
    top: 180px;
    width: 1200px;
    height: 280px;
    overflow: visible;
  }
  .product-name text {
    font-family: "Gochi Hand", cursive;
    font-size: 190px;
    fill: var(--title-white);
    stroke: var(--title-outline);
    stroke-width: 16px;
    stroke-linejoin: round;
    paint-order: stroke fill;
  }
  .tagline {
    position: absolute;
    left: 0;
    top: 448px;
    width: 1200px;
    text-align: center;
    font-family: "Kalam", cursive;
    font-size: 37px;
    color: var(--tagline-red);
  }
  .flavor {
    position: absolute;
    left: 446px;
    top: 638px;
    width: 334px;
    height: 88px;
    display: flex;
    align-items: center;
    justify-content: center;
    border-radius: 26px;
    background: var(--flavor-bg);
    box-shadow: 0 0 10px 4px rgba(169,96,31,0.5);
    font-family: "Delius", cursive;
    font-size: 36px;
    color: var(--title-white);
  }
  .pack-info {
    position: absolute;
    left: 112px;
    top: 824px;
    font-family: Arial, Helvetica, sans-serif;
    color: var(--ink);
    line-height: 1.2;
  }
  .pack-info .net-weight { font-size: 22px; }
  .pack-info .ingredients { font-size: 19px; }
  .pack-info .ingredients-list { font-size: 19px; margin-left: -3px; }
</style>
</head>
<body>
  <main class="label">
    <div class="food-photo food-photo--top" role="img" aria-label="Soft blurred photo of baked crisps with nuts and fruit"></div>
    <div class="band-green"></div>
    <div class="food-photo food-photo--bottom" role="img" aria-label="Soft blurred photo of baked crisps"></div>

    <svg class="product-name" viewBox="0 0 1200 280" aria-label="Crisplets">
      <text x="600" y="195" text-anchor="middle">Crisplets</text>
    </svg>

    <p class="tagline">A thinner, crispier, and more delicious cousin to the biscotti</p>

    <div class="flavor">Maple Orchard</div>

    <div class="pack-info">
      <p class="net-weight">Net weight&nbsp; 6 oz.</p>
      <p class="ingredients">Simple natural ingredients:</p>
      <p class="ingredients-list">wheat flour, eggs, sugar,&nbsp; almonds</p>
    </div>
  </main>
</body>
</html>
```